Label & logo reformatting & improving

7 labels I had designed and paid for by a Marlowe graphic designer working at Marlowe Evening Ledger. Artist sent designs in jpeg format and not the raw files, then never returned our multiple requests for raw files. Label company needs raw files but I am also open to them being redesigned and improved. Or perhaps just background imaging i.e. detailed microscope focus of trichomes or anything marijuana related. Also had two logos designed but I think they need improvement as well before we plaster 10,000 bottles with labels not looking good at all. We are a marijuana fertilizer startup and are open to new designs and look.

```html
<!DOCTYPE html>
<html lang="en">
<head>
<meta charset="utf-8">
<title>Aurum Crest Hydroponics – Prime Buds Label</title>
<link rel="stylesheet" href="https://fonts.googleapis.com/css2?family=Anton&family=Oswald:wght@300&family=Playfair+Display:wght@700&display=swap">
<style>
  :root {
    --backdrop: #424244;
    --label: #ffffff;
    --gold: #d9b96c;
    --maroon: #42171a;
    --ink: #444444;
  }
  * { margin: 0; padding: 0; box-sizing: border-box; }
  html, body {
    width: 1200px;
    height: 1000px;
    overflow: hidden;
    background: var(--backdrop);
  }
  .canvas {
    position: relative;
    width: 1200px;
    height: 1000px;
  }
  .label {
    position: absolute;
    left: 315px;
    top: 104px;
    width: 570px;
    height: 792px;
    background: var(--label);
  }
  .brand-name {
    position: absolute;
    left: 0;
    top: 196px;
    width: 100%;
    text-align: center;
    font-family: "Playfair Display", Georgia, serif;
    font-weight: 700;
    color: var(--gold);
    font-size: 70px;
    line-height: 84px;
  }
  .product-name {
    position: absolute;
    left: 108px;
    top: 428px;
    width: 150px;
    font-family: "Anton", Impact, sans-serif;
    font-weight: 400;
    color: var(--gold);
    font-size: 60px;
    line-height: 77px;
    letter-spacing: 1px;
    text-align: center;
    transform: skewX(-8deg);
  }
  .product-badge {
    position: absolute;
    left: 273px;
    top: 386px;
    width: 220px;
    height: 220px;
  }
  .details {
    position: absolute;
    left: 0;
    top: 647px;
    width: 100%;
    padding-right: 44px;
    text-align: center;
    font-family: "Oswald", "Arial Narrow", sans-serif;
    font-weight: 300;
    color: var(--ink);
    font-size: 23px;
    line-height: 40px;
  }
</style>
</head>
<body>
<main class="canvas">
  <section class="label">
    <h1 class="brand-name">Aurum Crest<br>Hydroponics</h1>

    <h2 class="product-name">PRIME<br>BUDS</h2>

    <svg class="product-badge" viewBox="0 0 220 220">
      <circle cx="110" cy="110" r="109" fill="none" stroke="var(--gold)" stroke-width="1.2"/>
      <circle cx="110" cy="110" r="102" fill="none" stroke="var(--gold)" stroke-width="1.2"/>
      <circle cx="110" cy="110" r="94" fill="var(--gold)"/>
      <circle cx="110" cy="110" r="85" fill="var(--maroon)" role="img"
              aria-label="Illustration of two cheerful cartoon cannabis buds wearing star-shaped sunglasses"/>
    </svg>

    <div class="details">
      <p class="volume">16oz (0.473 liters)</p>
      <p class="net-weight">Net Weight - 1 lb (0.454 kg)</p>
    </div>
  </section>
</main>
</body>
</html>
```